Natural and organic skincare brand needs label design!

I need labels designed for my natural and organic skincare brand lumavale. The front of the bottles must contain the logo (image attached) and the following words: Formulated by a Naturopath; Anti-aging therapy; Organic Facial Oil; with CoEnzyme Q10 and Rosehip Seed Oil; 100ml e3.38fl.oz. Colours I would like used include black/white/grey/silver and aqua. I also like the grey woodgrain used on my draft website (check out www.lumavale-skin.com.au). The logo should be silver foil (shiny).The final design should be simple and communicate nature and sophistication. Some designs I like are found in the attachments. I intend to use black or white bottles.

Target Market(s)

women aged 30-50 interested in natural products

Industry/Entity Type

Skin Care Product

Font styles to use
Serif
Sans Serif
Decorative
Script
Other font styles liked:
• Any

Requirements
Must have
• Dimensions: 62mm (w) x 75mm (H) (front label only)
• Must contain the logo (image attached). The logo should be silver foil (shiny). and the following words are to be included on the label:
• Formulated by a Naturopath;
• Anti-aging Therapy;
• Organic Facial Oil;
• with CoEnzyme Q10 and Rosehip Seed Oil;
• 100ml e3.38fl.oz.
Nice to have
• Colours I would like used include black/white/grey/silver and aqua (turquoise). But I am also open to suggestion. I also like the grey woodgrain used on my draft website (check out www.lumavale-skin.com.au)

```html
<!DOCTYPE html>
<html lang="en">
<head>
<meta charset="utf-8">
<title>lumavale – Anti-Aging Therapy Label Concept 3 (Black)</title>
<link rel="stylesheet" href="https://fonts.googleapis.com/css2?family=Oswald:wght@400;500&family=Roboto+Condensed:wght@400&family=Crimson+Text:wght@400&display=swap">
<style>
  :root {
    --canvas: #ffffff;
    --label-black: #0d0d0d;
    --pattern-grey: #262626;
    --ink-white: #ffffff;
    --ink-dark: #111111;
    --aqua: #2fc6b8;
    --green: #4cc34a;
    --lime: #9bcb2c;
    --gold: #c9a04a;
    --blue: #4a6fd0;
    --magenta: #c236b8;
    --red: #d04a4a;
  }
  * { box-sizing: border-box; margin: 0; padding: 0; }
  html, body {
    width: 1200px; height: 625px; overflow: hidden;
    background: var(--canvas);
  }
  .presentation { position: relative; width: 1200px; height: 625px; }
  .concept-title {
    position: absolute; top: 14px; left: 268px;
    font-family: "Oswald", sans-serif; font-weight: 400;
    font-size: 24px; line-height: 1.2; letter-spacing: 0.3px; color: var(--ink-dark);
  }
  .label {
    position: absolute;
    left: var(--x); top: var(--y);
    width: var(--w); height: var(--h);
    background: var(--label-black);
    overflow: hidden;
  }
  .label-pattern {
    position: absolute; inset: 0;
    background:
      radial-gradient(circle at 30% 35%, var(--pattern-grey) 0, transparent 32%),
      radial-gradient(circle at 75% 60%, var(--pattern-grey) 0, transparent 30%),
      radial-gradient(circle at 20% 78%, #1c1c1c 0, transparent 28%);
  }
  .label-bloom {
    position: absolute; top: 0; right: 0;
    width: calc(64px * var(--s)); height: calc(64px * var(--s));
    background: radial-gradient(circle at 100% 0%, var(--accent) 0%, var(--accent) 45%, transparent 72%);
  }
  .brand-mark {
    position: absolute;
    top: calc(14px * var(--s)); left: calc(10px * var(--s));
    width: calc(46px * var(--s)); height: calc(46px * var(--s));
    border-radius: 50%; background: var(--ink-white);
    display: flex; align-items: center; justify-content: center;
  }
  .brand-name {
    font-family: "Roboto Condensed", sans-serif; font-weight: 400;
    font-size: calc(9.5px * var(--s)); color: var(--ink-dark);
  }
  .title-stack {
    position: absolute;
    left: calc(10px * var(--s)); bottom: calc(84px * var(--s));
    writing-mode: vertical-rl; transform: rotate(180deg);
    white-space: nowrap; color: var(--ink-white);
  }
  .title-main, .title-sub { display: block; }
  .title-main {
    font-family: "Oswald", sans-serif; font-weight: 500;
    font-size: calc(24px * var(--s)); line-height: 1.05;
  }
  .title-sub {
    font-family: "Roboto Condensed", sans-serif; font-weight: 400;
    font-size: calc(11.5px * var(--s)); line-height: 1.15;
  }
  .product-type {
    position: absolute; left: 0; right: 0; bottom: calc(63px * var(--s));
    font-family: "Oswald", sans-serif; font-weight: 400;
    font-size: calc(11.5px * var(--s)); line-height: 1;
    color: var(--ink-white); text-align: center; white-space: nowrap;
  }
  .naturopath-band {
    position: absolute; left: 0; right: 0; bottom: calc(30px * var(--s));
    height: calc(28px * var(--s));
    background: var(--ink-white); color: var(--ink-dark);
    font-family: "Crimson Text", serif; font-size: calc(9.5px * var(--s));
    line-height: 1.1; text-transform: uppercase; letter-spacing: 0.3px;
    text-align: center;
    display: flex; flex-direction: column; justify-content: center;
  }
  .volume {
    position: absolute; left: 0; right: 0; bottom: calc(10px * var(--s));
    font-family: "Roboto Condensed", sans-serif; font-weight: 400;
    font-size: calc(10.5px * var(--s)); line-height: 1;
    color: var(--ink-white); text-align: center; white-space: nowrap;
  }
</style>
</head>
<body>
<main class="presentation">
  <h1 class="concept-title">CONCEPT: 3 (BLACK)</h1>

  <article class="label" style="--x:40px; --y:140px; --w:128px; --h:380px; --s:1; --accent: var(--aqua);">
    <div class="label-pattern" role="img" aria-label="Subtle dark grey floral pattern"></div>
    <div class="label-bloom" role="img" aria-label="Aqua flower bloom illustration"></div>
    <div class="brand-mark"><span class="brand-name">lumavale</span></div>
    <p class="title-stack"><span class="title-main">ANTI-AGING THERAPY</span><span class="title-sub">with CoEnzyme Q10 and Rosehip Seed Oil</span></p>
    <p class="product-type">ORGANIC FACIAL OIL</p>
    <p class="naturopath-band"><span>Formulated by</span><span>a Naturopath</span></p>
    <p class="volume">100ml e3.38 fl. oz.</p>
  </article>

  <article class="label" style="--x:190px; --y:195px; --w:128px; --h:330px; --s:0.9; --accent: var(--green);">
    <div class="label-pattern" role="img" aria-label="Subtle dark grey floral pattern"></div>
    <div class="label-bloom" role="img" aria-label="Green flower bloom illustration"></div>
    <div class="brand-mark"><span class="brand-name">lumavale</span></div>
    <p class="title-stack"><span class="title-main">ANTI-AGING THERAPY</span><span class="title-sub">with CoEnzyme Q10 and Rosehip Seed Oil</span></p>
    <p class="product-type">ORGANIC FACIAL OIL</p>
    <p class="naturopath-band"><span>Formulated by</span><span>a Naturopath</span></p>
    <p class="volume">100ml e3.38 fl. oz.</p>
  </article>

  <article class="label" style="--x:345px; --y:226px; --w:120px; --h:305px; --s:0.85; --accent: var(--lime);">
    <div class="label-pattern" role="img" aria-label="Subtle dark grey floral pattern"></div>
    <div class="label-bloom" role="img" aria-label="Lime flower bloom illustration"></div>
    <div class="brand-mark"><span class="brand-name">lumavale</span></div>
    <p class="title-stack"><span class="title-main">ANTI-AGING THERAPY</span><span class="title-sub">with CoEnzyme Q10 and Rosehip Seed Oil</span></p>
    <p class="product-type">ORGANIC FACIAL OIL</p>
    <p class="naturopath-band"><span>Formulated by</span><span>a Naturopath</span></p>
    <p class="volume">100ml e3.38 fl. oz.</p>
  </article>

  <article class="label" style="--x:494px; --y:62px; --w:194px; --h:483px; --s:1.3; --accent: var(--gold);">
    <div class="label-pattern" role="img" aria-label="Subtle dark grey floral pattern"></div>
    <div class="label-bloom" role="img" aria-label="Gold flower bloom illustration"></div>
    <div class="brand-mark"><span class="brand-name">lumavale</span></div>
    <p class="title-stack"><span class="title-main">ANTI-AGING THERAPY</span><span class="title-sub">with CoEnzyme Q10 and Rosehip Seed Oil</span></p>
    <p class="product-type">ORGANIC FACIAL OIL</p>
    <p class="naturopath-band"><span>Formulated by</span><span>a Naturopath</span></p>
    <p class="volume">100ml e3.38 fl. oz.</p>
  </article>

  <article class="label" style="--x:730px; --y:226px; --w:128px; --h:305px; --s:0.85; --accent: var(--blue);">
    <div class="label-pattern" role="img" aria-label="Subtle dark grey floral pattern"></div>
    <div class="label-bloom" role="img" aria-label="Blue flower bloom illustration"></div>
    <div class="brand-mark"><span class="brand-name">lumavale</span></div>
    <p class="title-stack"><span class="title-main">ANTI-AGING THERAPY</span><span class="title-sub">with CoEnzyme Q10 and Rosehip Seed Oil</span></p>
    <p class="product-type">ORGANIC FACIAL OIL</p>
    <p class="naturopath-band"><span>Formulated by</span><span>a Naturopath</span></p>
    <p class="volume">100ml e3.38 fl. oz.</p>
  </article>

  <article class="label" style="--x:885px; --y:196px; --w:128px; --h:330px; --s:0.9; --accent: var(--magenta);">
    <div class="label-pattern" role="img" aria-label="Subtle dark grey floral pattern"></div>
    <div class="label-bloom" role="img" aria-label="Magenta flower bloom illustration"></div>
    <div class="brand-mark"><span class="brand-name">lumavale</span></div>
    <p class="title-stack"><span class="title-main">ANTI-AGING THERAPY</span><span class="title-sub">with CoEnzyme Q10 and Rosehip Seed Oil</span></p>
    <p class="product-type">ORGANIC FACIAL OIL</p>
    <p class="naturopath-band"><span>Formulated by</span><span>a Naturopath</span></p>
    <p class="volume">100ml e3.38 fl. oz.</p>
  </article>

  <article class="label" style="--x:1035px; --y:155px; --w:128px; --h:370px; --s:1; --accent: var(--red);">
    <div class="label-pattern" role="img" aria-label="Subtle dark grey floral pattern"></div>
    <div class="label-bloom" role="img" aria-label="Red flower bloom illustration"></div>
    <div class="brand-mark"><span class="brand-name">lumavale</span></div>
    <p class="title-stack"><span class="title-main">ANTI-AGING THERAPY</span><span class="title-sub">with CoEnzyme Q10 and Rosehip Seed Oil</span></p>
    <p class="product-type">ORGANIC FACIAL OIL</p>
    <p class="naturopath-band"><span>Formulated by</span><span>a Naturopath</span></p>
    <p class="volume">100ml e3.38 fl. oz.</p>
  </article>
</main>
</body>
</html>
```